complete redesign of VitaPlate.com

VITAPLATE.COM
MAIN MANU

We need it cut into HTML / Wordpress Friendly.... Our developer will handle all the WP / PHP coding, but we need it placed into HTML format so he can put into wordpress.

Please see the old vitaplate.com by visiting www.vitaplate.com... we want something completely different, but... just use this site for reference as to audience, theme, etc... we want something where it is science meets diet in helping fight cancer :)

WE NEED SOMETHING MORE MODERN AND MEDICAL IN TERMS OF DESIGN

See below:

1 CANCER NEWS
2 NUTRITION DIAGNOSTICS
3 DIET STEPS
4 DIET SUPPLEMENTS IN CANCER 
5 DICTIONARY OF MARKINGS ON FOOD
6 MERIVOLA VIDEOS
7 YOUR INDIVIDUAL DIET - SUBSCRIPTION

a. CANCER NEWS - latest articles relating to cancer prevention research treatments

b. NUTRITION DIAGNOSTICS -  description of the research that must be done to determine the degree of malnutrition of the body a place on the charts
pictures, etc.

c. DIET STEPS 
(sub menu - @)
¥ prevention of oncological - @
¥ diet chemotherapy - @
¥ diet in radiotherapy - @
¥ hormonal diet - @
¥ diet during convalescence - @

d. DIET SUPPLEMENTS IN CANCER - articles describing various supplements summary tables, etc.

e. DICTIONARY OF MARKINGS ON FOOD - composition, translation of labels on food, itd.

f. MERIVOLA VIDEOS 
(sub menu - @)
¥ healthy cooking - @
¥ meal preparation - @
¥ storage of food - @
¥ eco food - @
¥ rehabilitation - @
¥ yoga - @
¥ exercises - @
¥ psycho-oncology training - @
¥ music therapy - @

g. YOUR INDIVIDUAL DIET -  individual personalized diet for subscribing. We
add this point by developing a system of diet.

After 3 months, we will add special individual programs that mix diet, exercise and psychological lectures

Industry/Entity Type

Medical

Logo Text

Vita Plate / VitaPlate.com

Number of Pages Required

5+ page

Font styles to use
Sans Serif

Colors
ec1f27
9bcb3c
ffffff

Requirements
Must have
• HTML/CSS

```html
<!DOCTYPE html>
<html lang="en">
<head>
<meta charset="utf-8">
<title>Vita Plate — The science behind what we eat</title>
<link href="https://fonts.googleapis.com/css2?family=Open+Sans:wght@300;400;600;700;800&display=swap" rel="stylesheet">
<style>
:root{
  --green:#a3dc8e;
  --green-mid:#8fd176;
  --green-deep:#5fae4a;
  --green-text:#7cc865;
  --ink:#333a33;
  --ink-soft:#5b625b;
  --muted:#8a8f8a;
  --white:#ffffff;
  --page-bg:#eeeeee;
}
*{box-sizing:border-box;margin:0;padding:0}
html,body{width:1200px;height:3947px;overflow:hidden}
body{background:var(--page-bg);font-family:"Open Sans",Arial,sans-serif;color:var(--ink)}
.page{position:absolute;left:13px;top:0;width:1174px;height:3927px;background:var(--white)}
section,header,nav,footer{position:relative;width:100%}

/* header */
.site-header{height:166px}
.brand{position:absolute;left:32px;top:38px;display:flex;align-items:center;gap:18px}
.brand-mark{width:90px;height:90px;border-radius:50%;background:var(--green)}
.brand-name{font-size:38px;font-weight:300;letter-spacing:5px;color:var(--ink);line-height:1}
.brand-tag{font-size:14px;font-weight:600;color:var(--green-deep);margin-top:8px;letter-spacing:.3px}
.social{position:absolute;right:28px;top:64px;display:flex;gap:10px}
.social span{width:28px;height:28px;border-radius:50%;background:var(--green)}

/* nav */
.main-nav{height:37px;background:var(--green);display:flex;justify-content:space-between;align-items:center;padding:0 22px}
.main-nav a{color:var(--white);font-size:12.5px;font-weight:600;text-decoration:none;text-transform:uppercase}

/* hero: soft tonal wash in the banner's main colours */
.hero{height:415px;background:
  radial-gradient(ellipse 230px 260px at 300px 150px,rgba(214,150,108,.85),rgba(214,150,108,0) 70%),
  radial-gradient(ellipse 170px 150px at 250px 330px,rgba(250,250,248,.95),rgba(250,250,248,0) 70%),
  radial-gradient(ellipse 260px 190px at 800px 250px,rgba(142,184,52,.9),rgba(142,184,52,0) 72%),
  radial-gradient(ellipse 180px 140px at 610px 250px,rgba(240,206,60,.9),rgba(240,206,60,0) 72%),
  radial-gradient(ellipse 120px 110px at 960px 150px,rgba(196,70,40,.75),rgba(196,70,40,0) 70%),
  radial-gradient(ellipse 340px 140px at 760px 410px,rgba(150,98,52,.7),rgba(150,98,52,0) 72%),
  linear-gradient(90deg,#f4efe8 0%,#ece2d6 40%,#f3efe6 62%,#f6f4ef 100%)}
.hero-arrow{position:absolute;top:170px}
.hero-arrow.left{left:8px}.hero-arrow.right{right:8px}

/* intro band */
.intro{height:137px;background:var(--green);text-align:center;padding-top:24px}
.intro h1{font-size:28px;font-weight:800;color:var(--ink);letter-spacing:.5px}
.intro h1 em{font-style:normal;color:var(--white)}
.intro p{color:var(--white);font-size:15px;line-height:22px;width:1020px;margin:6px auto 0}

.divider{position:absolute;left:50%;top:-20px;margin-left:-20px;width:40px;height:40px;border-radius:50%;background:var(--white);border:3px solid var(--green);z-index:2}
.section-title{font-size:22px;font-weight:800;text-transform:uppercase;text-align:center;color:var(--ink)}
.section-title em{font-style:normal;color:var(--green-text)}
.green .section-title em{color:var(--white)}
.green{background:var(--green)}

/* cards */
.card{position:absolute;background:var(--white);padding:9px;box-shadow:0 2px 8px rgba(0,0,0,.25)}
.card .photo{position:relative;width:100%;height:100%}
.caption{position:absolute;left:0;right:0;bottom:0;height:44px;background:rgba(120,200,95,.88);color:var(--white);font-size:14px;font-weight:700;text-transform:uppercase;padding:13px 12px 0}

/* photo tone washes */
.ph-lab{background:
  radial-gradient(ellipse 35% 30% at 30% 28%,rgba(120,200,210,.9),rgba(120,200,210,0) 70%),
  radial-gradient(ellipse 40% 45% at 80% 80%,rgba(96,160,60,.9),rgba(96,160,60,0) 70%),
  radial-gradient(ellipse 25% 30% at 25% 75%,rgba(70,70,70,.55),rgba(70,70,70,0) 70%),
  linear-gradient(135deg,#f5f7f5,#e6eeea)}
.ph-plate{background:
  radial-gradient(ellipse 45% 40% at 50% 60%,rgba(212,126,52,.95),rgba(212,126,52,0) 72%),
  radial-gradient(ellipse 30% 25% at 55% 50%,rgba(240,236,228,.8),rgba(240,236,228,0) 72%),
  radial-gradient(ellipse 22% 20% at 82% 18%,rgba(90,150,50,.85),rgba(90,150,50,0) 70%),
  linear-gradient(135deg,#141311,#2c241d 60%,#1a1714)}
.ph-sun{background:
  radial-gradient(ellipse 40% 40% at 45% 40%,rgba(232,104,40,.85),rgba(232,104,40,0) 72%),
  radial-gradient(ellipse 45% 40% at 85% 25%,rgba(255,236,170,.95),rgba(255,236,170,0) 72%),
  linear-gradient(135deg,#f4b457,#f6c970 60%,#fbe2a0)}
.ph-grain{background:
  radial-gradient(circle at 25% 30%,rgba(214,190,140,.9),rgba(214,190,140,0) 22%),
  radial-gradient(circle at 70% 40%,rgba(150,60,50,.85),rgba(150,60,50,0) 20%),
  radial-gradient(circle at 40% 75%,rgba(230,220,195,.9),rgba(230,220,195,0) 20%),
  radial-gradient(circle at 80% 80%,rgba(60,60,90,.8),rgba(60,60,90,0) 18%),
  linear-gradient(135deg,#4a3828,#6b523a)}
.ph-spice{background:
  radial-gradient(circle at 30% 30%,rgba(200,90,50,.9),rgba(200,90,50,0) 22%),
  radial-gradient(circle at 70% 60%,rgba(210,190,150,.9),rgba(210,190,150,0) 22%),
  radial-gradient(circle at 25% 80%,rgba(120,130,70,.85),rgba(120,130,70,0) 20%),
  linear-gradient(135deg,#3a322c,#5a4a3c)}
.ph-tomato{background:
  radial-gradient(circle at 30% 35%,rgba(222,52,30,.95),rgba(222,52,30,0) 24%),
  radial-gradient(circle at 65% 55%,rgba(200,36,24,.95),rgba(200,36,24,0) 26%),
  radial-gradient(circle at 45% 80%,rgba(230,70,36,.9),rgba(230,70,36,0) 22%),
  radial-gradient(ellipse 40% 20% at 80% 20%,rgba(230,130,50,.85),rgba(230,130,50,0) 70%),
  linear-gradient(135deg,#2a2620,#3f3527)}
.ph-carrot{background:
  repeating-linear-gradient(160deg,rgba(232,110,30,.0) 0 18px,rgba(232,110,30,.35) 18px 40px),
  radial-gradient(ellipse 50% 40% at 70% 30%,rgba(240,130,40,.9),rgba(240,130,40,0) 72%),
  linear-gradient(135deg,#f1a050,#e97a2c 55%,#f6d7b0)}
.ph-fish{background:
  radial-gradient(circle at 25% 35%,rgba(236,126,90,.95),rgba(236,126,90,0) 24%),
  radial-gradient(circle at 70% 30%,rgba(90,140,60,.85),rgba(90,140,60,0) 20%),
  radial-gradient(circle at 60% 75%,rgba(200,170,110,.9),rgba(200,170,110,0) 22%),
  radial-gradient(circle at 88% 60%,rgba(150,40,40,.8),rgba(150,40,40,0) 16%),
  linear-gradient(135deg,#3e342b,#5a4a3a)}

.news{height:653px}
.news .section-title{position:absolute;top:42px;width:100%}
.col1{left:32px;width:363px}.col2{left:413px;width:356px}.col3{left:784px;width:353px}

/* diagnostics */
.diagnostics{height:428px}
.chart-figure{position:absolute;left:45px;top:34px;width:318px;height:353px;background:
  radial-gradient(ellipse 30% 28% at 45% 40%,rgba(226,186,186,.8),rgba(226,186,186,0) 70%),
  radial-gradient(ellipse 22% 30% at 50% 70%,rgba(206,190,200,.7),rgba(206,190,200,0) 70%),
  #ffffff;border:1px solid #dcdcdc}
.text-block{position:absolute;left:421px;width:700px}
.text-block h2{font-size:21px;font-weight:800;text-transform:uppercase;color:var(--ink);margin-bottom:14px}
.text-block h2 em{font-style:normal;color:var(--white)}
.dictionary .text-block h2 em{color:var(--green-text)}
.text-block p{font-size:14px;line-height:21px;color:var(--ink-soft);margin-bottom:13px}
.diagnostics .text-block p{color:#3f4a3c}
.btn-outline{display:inline-block;border:2px solid var(--ink);border-radius:6px;padding:7px 13px;font-size:14px;font-weight:700;text-transform:uppercase;color:var(--ink)}

/* steps */
.steps{height:327px}
.steps .section-title{position:absolute;top:38px;width:100%}
.tile{position:absolute;top:93px;height:192px}
.tile .caption{height:32px;font-size:14px;font-weight:600;text-transform:none;padding:6px 10px 0;text-align:center}

/* supplements */
.supplements{height:390px}
.supplements .section-title{position:absolute;top:44px;width:100%}

/* dictionary */
.dictionary{height:316px}
.label-figure{position:absolute;left:45px;top:40px;width:332px;height:252px;background:
  linear-gradient(90deg,rgba(255,255,255,0) 22%,#ffffff 22% 24%,rgba(255,255,255,0) 24%),
  radial-gradient(ellipse 30% 40% at 50% 35%,rgba(190,210,235,.85),rgba(190,210,235,0) 70%),
  radial-gradient(ellipse 30% 25% at 50% 72%,rgba(240,190,190,.7),rgba(240,190,190,0) 70%),
  radial-gradient(ellipse 12% 35% at 10% 45%,rgba(240,160,90,.55),rgba(240,160,90,0) 70%),
  radial-gradient(ellipse 12% 35% at 90% 45%,rgba(90,190,220,.55),rgba(90,190,220,0) 70%),
  #ffffff;border:1px solid #dcdcdc}

/* videos */
.videos{height:631px}
.videos .section-title{position:absolute;top:55px;left:0;width:100%}
.video-filters{position:absolute;right:55px;top:56px;display:flex;gap:14px}
.pill{width:160px;height:26px;border-radius:13px;font-size:11px;font-weight:700;display:flex;align-items:center;justify-content:center;gap:8px;text-transform:uppercase}
.pill.on{background:var(--white);color:var(--ink);box-shadow:0 1px 3px rgba(0,0,0,.3)}
.pill.off{background:#c8c8c8;color:var(--ink);box-shadow:0 1px 3px rgba(0,0,0,.3)}
.pill i{width:14px;height:14px;border-radius:3px;background:var(--ink);display:block}
.video-grid{position:absolute;top:105px;left:0;width:1174px;display:grid;grid-template-columns:repeat(3,1fr);grid-template-rows:263px 263px}
.video{position:relative;display:flex;align-items:center;justify-content:center}

/* subscribe */
.subscribe{height:74px;background:var(--green-mid);display:flex;align-items:center;padding:0 22px}
.subscribe h3{color:var(--white);font-size:21px;font-weight:700;width:535px}
.field{height:42px;background:var(--white);font-size:13px;color:var(--ink);padding:12px 12px 0}
.field.name{width:226px;margin-right:12px}.field.email{width:230px;margin-right:12px}
.btn-subscribe{height:42px;width:106px;background:#3f9a35;color:var(--white);font-size:13px;font-weight:700;text-align:center;padding-top:12px}

/* footer */
.site-footer{height:326px}
.footer-brand{position:absolute;left:68px;top:68px;width:150px;text-align:center}
.footer-brand .brand-mark{width:80px;height:80px;margin:0 auto 8px}
.footer-brand .brand-name{font-size:15px;letter-spacing:2px;font-weight:600}
.fcol{position:absolute;top:52px}
.fcol h4{font-size:13px;font-weight:800;text-transform:uppercase;margin-bottom:12px}
.fcol li{list-style:none;font-size:11.5px;color:var(--muted);text-transform:uppercase;line-height:20px}
.nav-col{left:277px}.contact-form{left:567px;width:230px}.info-col{left:856px}
.ff{height:22px;background:#e9e9e9;margin-bottom:6px;font-size:11px;color:var(--ink-soft);padding:4px 8px 0}
.ff.msg{height:60px}
.btn-send{width:102px;height:32px;background:#1e1e1e;color:var(--white);font-size:12px;font-weight:700;text-align:center;padding-top:8px;margin-top:10px}
.info-row{display:flex;align-items:center;gap:10px;font-size:11.5px;color:var(--muted);margin-bottom:16px}
.info-social{display:flex;gap:10px;margin-left:28px}
.info-social span{width:18px;height:18px;border-radius:50%;background:#9a9a9a}

.copyright{height:27px;background:var(--green);color:var(--white);font-size:10px;text-align:center;padding-top:7px;text-transform:uppercase}
</style>
</head>
<body>
<div class="page">

<header class="site-header">
  <div class="brand">
    <span class="brand-mark"></span>
    <div>
      <div class="brand-name">VITA PLATE</div>
      <div class="brand-tag">The science behind what we eat</div>
    </div>
  </div>
  <div class="social" aria-label="Social links"><span></span><span></span><span></span><span></span></div>
</header>

<nav class="main-nav">
  <a href="#">Cancer News</a><a href="#">Nutrition Diagnostics</a><a href="#">Diet Steps</a><a href="#">Diet Supplements in Cancer</a><a href="#">Dictionary of Markings on Food</a><a href="#">Merivola Videos</a><a href="#">Your Individual Diet</a>
</nav>

<section class="hero" role="img" aria-label="Smiling woman holding a basket of fresh fruit">
  <svg class="hero-arrow left" width="24" height="60" viewBox="0 0 24 60"><polyline points="20,4 4,30 20,56" fill="none" stroke="#fff" stroke-width="2"/></svg>
  <svg class="hero-arrow right" width="24" height="60" viewBox="0 0 24 60"><polyline points="4,4 20,30 4,56" fill="none" stroke="#fff" stroke-width="2"/></svg>
</section>

<section class="intro">
  <h1>YOU ARE <em>WHAT YOU EAT</em></h1>
  <p>At VitaPlate.com we are diving into the science and chemistry of what we eat and how it effects our bodies in ways we could not imagine until recently. It is true - you are what you eat, and we intend to show you how you can eat your way to a healthy and cancer free life.</p>
</section>

<section class="news">
  <span class="divider"></span>
  <h2 class="section-title">Cancer <em>News</em></h2>
  <article class="card col1" style="top:90px;height:245px"><div class="photo ph-lab" role="img" aria-label="Scientist with microscope and plants"><div class="caption">12.25.2015 News Article #1</div></div></article>
  <article class="card col2" style="top:90px;height:245px"><div class="photo ph-plate" role="img" aria-label="Plate of healthy pasta"><div class="caption">12.25.2015 News Article #2</div></div></article>
  <article class="card col3" style="top:90px;height:245px"><div class="photo ph-sun" role="img" aria-label="Woman enjoying the sunlight"><div class="caption">12.25.2015 News Article #3</div></div></article>
  <article class="card col1" style="top:356px;height:252px"><div class="photo ph-sun" role="img" aria-label="Woman enjoying the sunlight"><div class="caption">12.25.2015 News Article #4</div></div></article>
  <article class="card col2" style="top:356px;height:252px"><div class="photo ph-lab" role="img" aria-label="Scientist with microscope and plants"><div class="caption">12.25.2015 News Article #5</div></div></article>
  <article class="card col3" style="top:356px;height:252px"><div class="photo ph-plate" role="img" aria-label="Plate of healthy pasta"><div class="caption">12.25.2015 News Article #6</div></div></article>
</section>

<section class="diagnostics green">
  <span class="divider"></span>
  <div class="chart-figure" role="img" aria-label="Labelled diagram of the digestive and nervous system"></div>
  <div class="text-block" style="top:44px">
    <h2>Nutrition <em>Diagnostics</em></h2>
    <p>Lorem ipsum dolor sit amet, consectetuer adipiscing elit, sed diam nonummy nibh euismod tincidunt ut laoreet dolore magna aliquam erat volutpat. Ut wisi enim ad minim veniam, quis nostrud exerci tation ullamcorper suscipit lobortis nisl ut aliquip ex ea commodo consequat.</p>
    <p>Duis autem vel eum iriure dolor in hendrerit in vulputate velit esse molestie consequat, vel illum dolore eu feugiat nulla facilisis at vero eros et accumsan et iusto odio dignissim qui blandit praesent luptatum zzril delenit augue duis dolore te feugait nulla facilisi. Nam liber tempor cum soluta nobis eleifend option congue nihil imperdiet doming id quod mazim placerat facer possim assum. Typi non habent claritatem insitam; est usus legentis in iis qui facit eorum claritatem. Investigationes demonstraverunt lectores legere me lius quod ii legunt saepius.</p>
    <span class="btn-outline">Read More</span>
  </div>
</section>

<section class="steps">
  <span class="divider"></span>
  <h2 class="section-title">Diet <em>Steps</em></h2>
  <div class="tile ph-grain" style="left:34px;width:211px" role="img" aria-label="Bowls of grains and seeds"><div class="caption">Prevention of Oncological</div></div>
  <div class="tile ph-sun" style="left:261px;width:208px" role="img" aria-label="Woman enjoying the sunlight"><div class="caption">Diet Chemotherapy</div></div>
  <div class="tile ph-spice" style="left:484px;width:208px" role="img" aria-label="Spoons of spices and legumes"><div class="caption">Diet in Radiotherapy</div></div>
  <div class="tile ph-tomato" style="left:705px;width:208px" role="img" aria-label="Cherry tomatoes on the vine"><div class="caption">Hormonal Diet</div></div>
  <div class="tile ph-carrot" style="left:929px;width:208px" role="img" aria-label="Fresh carrots"><div class="caption">Diet During Convalescence</div></div>
</section>

<section class="supplements green">
  <span class="divider"></span>
  <h2 class="section-title">Diet Supplements in <em>Cancer</em></h2>
  <article class="card col1" style="top:90px;height:253px"><div class="photo ph-lab" role="img" aria-label="Scientist with microscope and plants"><div class="caption">Article #1</div></div></article>
  <article class="card col2" style="top:90px;height:253px"><div class="photo ph-plate" role="img" aria-label="Plate of healthy pasta"><div class="caption">Article #2</div></div></article>
  <article class="card col3" style="top:90px;height:253px"><div class="photo ph-sun" role="img" aria-label="Woman enjoying the sunlight"><div class="caption">Article #3</div></div></article>
</section>

<section class="dictionary">
  <span class="divider"></span>
  <div class="label-figure" role="img" aria-label="Annotated nutrition facts label"></div>
  <div class="text-block" style="left:395px;top:44px">
    <h2>Dictionary of Markings on <em>Food</em></h2>
    <p>Lorem ipsum dolor sit amet, consectetuer adipiscing elit, sed diam nonummy nibh euismod tincidunt ut laoreet dolore magna aliquam erat volutpat. Ut wisi enim ad minim veniam, quis nostrud exerci tation ullamcorper suscipit lobortis nisl ut aliquip ex ea commodo consequat.</p>
    <span class="btn-outline" style="margin-top:22px">Read More</span>
  </div>
</section>

<section class="videos green">
  <span class="divider"></span>
  <h2 class="section-title">Merivola <em>Videos</em></h2>
  <div class="video-filters">
    <span class="pill on"><svg width="14" height="14" viewBox="0 0 14 14"><polyline points="2,7 6,11 12,2" fill="none" stroke="#3f9a35" stroke-width="2.5"/></svg>All Videos</span>
    <span class="pill off"><i></i>By Category</span>
  </div>
  <div class="video-grid">
    <div class="video ph-tomato" role="img" aria-label="Video: tomatoes and carrots"><svg width="76" height="76" viewBox="0 0 76 76"><circle cx="38" cy="38" r="36" fill="#fff" fill-opacity=".85"/><polygon points="30,24 54,38 30,52" fill="#3a3a3a"/></svg></div>
    <div class="video ph-sun" role="img" aria-label="Video: woman in the sunlight"><svg width="76" height="76" viewBox="0 0 76 76"><circle cx="38" cy="38" r="36" fill="#fff" fill-opacity=".85"/><polygon points="30,24 54,38 30,52" fill="#3a3a3a"/></svg></div>
    <div class="video ph-fish" role="img" aria-label="Video: salmon, grains and vegetables"><svg width="76" height="76" viewBox="0 0 76 76"><circle cx="38" cy="38" r="36" fill="#fff" fill-opacity=".85"/><polygon points="30,24 54,38 30,52" fill="#3a3a3a"/></svg></div>
    <div class="video ph-fish" role="img" aria-label="Video: healthy food ingredients"><svg width="76" height="76" viewBox="0 0 76 76"><circle cx="38" cy="38" r="36" fill="#fff" fill-opacity=".85"/><polygon points="30,24 54,38 30,52" fill="#3a3a3a"/></svg></div>
    <div class="video ph-tomato" role="img" aria-label="Video: cherry tomatoes and carrots"><svg width="76" height="76" viewBox="0 0 76 76"><circle cx="38" cy="38" r="36" fill="#fff" fill-opacity=".85"/><polygon points="30,24 54,38 30,52" fill="#3a3a3a"/></svg></div>
    <div class="video ph-sun" role="img" aria-label="Video: woman in the sunlight"><svg width="76" height="76" viewBox="0 0 76 76"><circle cx="38" cy="38" r="36" fill="#fff" fill-opacity=".85"/><polygon points="30,24 54,38 30,52" fill="#3a3a3a"/></svg></div>
  </div>
</section>

<section class="subscribe">
  <h3>Subscribe for your individual personalized diet</h3>
  <div class="field name">Name</div>
  <div class="field email">Email</div>
  <div class="btn-subscribe">SUBSCRIBE</div>
</section>

<footer class="site-footer">
  <div class="footer-brand"><span class="brand-mark" style="display:block"></span><div class="brand-name">VITA PLATE</div></div>
  <div class="fcol nav-col">
    <h4>Navigation</h4>
    <ul><li>Cancer News</li><li>Nutrition Diagnostics</li><li>Diet Steps</li><li>Diet Supplements in Cancer</li><li>Dictionary of Markings on Food</li><li>Merivola Videos</li><li>Your Individual Diet</li></ul>
  </div>
  <div class="fcol contact-form">
    <h4>Quick Contact</h4>
    <div class="ff">Name</div><div class="ff">Email</div><div class="ff">Phone</div><div class="ff msg">Message</div>
    <div class="btn-send">SEND</div>
  </div>
  <div class="fcol info-col">
    <h4>Contact Info</h4>
    <div class="info-row"><svg width="18" height="16" viewBox="0 0 18 16"><path d="M2 5c0-2 2-3 7-3s7 1 7 3v1h-4V4H6v2H2z M4 8h10l2 6H2z" fill="#888"/></svg>+48 500 120 340</div>
    <div class="info-row"><svg width="18" height="13" viewBox="0 0 18 13"><rect x="1" y="1" width="16" height="11" fill="none" stroke="#888" stroke-width="1.5"/><polyline points="1,1 9,7 17,1" fill="none" stroke="#888" stroke-width="1.5"/></svg>info@vitaplate.com</div>
    <div class="info-social"><span></span><span></span><span></span></div>
  </div>
</footer>

<div class="copyright">© 2015 VITAPLATE. All rights reserved.</div>
</div>
</body>
</html>
```